Law Firm Website, easily updated by User

We are a regional Labor and Employment Law Firm with a tired outdated website. We are looking for a clean easy to use website that will allow us to easily update information and articles in house. Our current website can be found at www.quillbrookcounsel.com

Industry/Entity Type

Labor

Number of Pages Required

5+ page

Colors
0655a3

Requirements
Must have
• Content easily updated by user
Nice to have
• crisp clean pages
Should not have
• stock pictures

```html
<!DOCTYPE html>
<html lang="en">
<head>
<meta charset="utf-8">
<title>Quillbrook &amp; Associates, P.C. — Labor &amp; Employment Law</title>
<link href="https://fonts.googleapis.com/css2?family=Open+Sans:wght@400;600&family=Roboto:wght@300;400&family=Tinos&display=swap" rel="stylesheet">
<style>
:root{
  --blue:#0655a3;
  --blue-dark:#1b4b98;
  --link:#1d4b94;
  --text:#4a4a4a;
  --muted:#777;
  --line:#dcdcdc;
  --section:#f2f2f2;
  --footer:#3d3d3d;
  --footer-bottom:#2f2f2f;
  --footer-text:#a9a9a9;
}
*{margin:0;padding:0;box-sizing:border-box}
html,body{width:922px;height:1200px;overflow:hidden;background:#fff}
body{position:relative;font-family:Roboto,sans-serif;color:var(--text)}
.abs{position:absolute}
h2,h3{font-family:"Open Sans",sans-serif;font-weight:400;color:#2b2b2b}

.hero{left:0;top:0;width:922px;height:446px;background:linear-gradient(100deg,#5a4a40 0%,#8c8378 25%,#c9c7c2 50%,#9a9389 72%,#6b5e55 100%)}
.header{left:46px;top:0;width:831px;height:81px;background:rgba(255,255,255,.97);box-shadow:0 1px 3px rgba(0,0,0,.15)}
.brand{left:11px;top:30px;display:flex;align-items:center;gap:6px}
.brand-mark{width:20px;height:20px;background:var(--blue-dark)}
.brand-name{font-family:Tinos,serif;font-size:17px;color:#1a2a55;line-height:1}
.brand-tag{left:11px;top:58px;font-family:Tinos,serif;font-size:5.6px;color:#1a2a55;letter-spacing:.1px}
.contact{right:12px;top:16px;font-size:11px;color:var(--blue-dark)}
.contact b{font-weight:400}
.contact small{font-size:9px}
.nav{left:243px;top:57px;display:flex;font-size:10px;color:#444}
.nav span{padding:0 12px}
.nav .active{color:var(--blue);position:relative}
.nav .active:after{content:"";position:absolute;left:0;right:0;top:19px;height:3px;background:var(--blue)}

.caption{left:57px;top:321px;width:413px;height:63px;background:rgba(255,255,255,.9);clip-path:polygon(0 0,100% 0,88% 100%,0 100%);padding:6px 0 0 14px;font-family:"Open Sans",sans-serif;font-size:21px;line-height:25px}
.caption .l1{color:#2b2b2b}
.caption .l2{color:var(--blue-dark)}
.dots{left:801px;top:370px;display:flex;gap:4px}
.dots i{width:13px;height:13px;border-radius:50%;background:#ddd}
.dots i:first-child{background:#222}

.card{background:#fff;border:1px solid var(--line);box-shadow:0 0 2px rgba(0,0,0,.08)}
.welcome{left:57px;top:408px;width:532px;height:235px}
.news{left:611px;top:408px;width:254px;height:235px}
.card h2{position:absolute;font-size:18px;line-height:22px}
.welcome h2{left:14px;top:16px}
.welcome p{position:absolute;left:14px;top:45px;width:262px;font-size:8.6px;line-height:16.4px;color:#555}
.welcome .photo{position:absolute;left:286px;top:18px;width:231px;height:152px;background:linear-gradient(135deg,#7a2530,#c9a45c 45%,#26305e 100%)}
.btn{position:absolute;height:28px;padding:0 15px;background:var(--blue-dark);color:#fff;font-size:10.5px;line-height:28px;border-radius:2px}
.welcome .btn{left:14px;top:190px}
.news h2{left:16px;top:14px}
.news-item{position:absolute;left:17px;width:222px}
.news-item .date{font-size:11px;color:var(--blue-dark)}
.news-item p{font-size:8.6px;line-height:13.6px;color:#555;margin-top:3px}
.news-item .more{font-size:8.8px;color:var(--blue-dark);margin-top:4px}
.news .i1{top:46px;padding-bottom:10px;border-bottom:1px solid var(--line)}
.news .i2{top:124px}
.news .btn{left:19px;top:190px}

.section{left:0;top:655px;width:922px;height:305px;background:var(--section)}
.practice{left:57px;top:676px;width:390px;height:260px}
.practice h2,.attorneys h2{font-size:18px;line-height:22px}
.lead{font-size:8.6px;line-height:16px;color:#888;margin-top:6px}
.plist{position:absolute;top:82px;width:205px;list-style:none;font-size:9px;line-height:12px;color:var(--link)}
.plist li{height:19.2px;white-space:nowrap}
.plist li:before{content:"»";margin-right:7px;font-size:8px}
.pl1{left:0}.pl2{left:205px}
.practice .btn{left:0;top:229px}
.divider{left:472px;top:680px;width:1px;height:252px;background:var(--line)}
.attorneys{left:495px;top:676px;width:372px;height:260px}
.acard{position:absolute;width:180px;height:71px;background:#fff;border:1px solid var(--line)}
.acard .pic{position:absolute;left:8px;top:7px;width:56px;height:56px;background:linear-gradient(160deg,#d9b9a0,#8a6a55)}
.acard .name{position:absolute;left:76px;top:15px;font-size:10px;color:var(--blue-dark)}
.acard .role{position:absolute;left:76px;top:28px;font-size:8.8px;color:#888}
.acard .deg{position:absolute;left:76px;top:45px;font-size:8.8px;color:#888}
.attorneys .btn{left:0;top:229px}

.footer{left:0;top:960px;width:922px;height:192px;background:var(--footer);border-top:3px solid var(--blue-dark)}
.fcol{position:absolute;top:25px}
.fcol h3{font-size:13px;line-height:18px;color:#fff;margin-bottom:2px}
.fcol div{font-size:8.6px;line-height:18.4px;color:var(--footer-text)}
.social{display:flex;gap:10px;margin-top:8px}
.social i{width:22px;height:22px;border-radius:3px;background:#5d6f8f}
.social i:nth-child(2){background:#4a9bc4}
.social i:nth-child(3){background:#3d6f9a}
.social i:nth-child(4){background:#d67a2a}
.bottom{left:0;top:1152px;width:922px;height:48px;background:var(--footer-bottom);font-size:8.4px;color:var(--footer-text)}
.bottom .copy{position:absolute;left:56px;top:19px}
.bottom .legal{position:absolute;right:56px;top:19px}
</style>
</head>
<body>

<div class="abs hero" role="img" aria-label="Photo of an attorney in a suit meeting with two clients across a desk"></div>

<header class="abs header">
  <div class="abs brand"><span class="brand-mark"></span><span class="brand-name">Quillbrook &amp; Associates, P.C.</span></div>
  <div class="abs brand-tag">EMPLOYMENT COUNSELING, LITIGATION, LABOR &amp; BENEFITS LAW</div>
  <div class="abs contact"><b>CALL: (631) 555-0148</b> &nbsp;| &nbsp;<b>EMAIL:</b> <small>info@quillbrookcounsel.com</small></div>
  <nav class="abs nav">
    <span class="active">HOME</span><span>ATTORNEYS</span><span>AREAS OF PRACTICE »</span><span>IN THE NEWS</span><span>FAQ</span><span>FOR EMPLOYERS</span><span>CONTACT US</span>
  </nav>
</header>

<div class="abs caption"><div class="l1">Counselling &amp; Advising Clients</div><div class="l2">Exclusively on Law of the Workshop</div></div>
<div class="abs dots"><i></i><i></i><i></i><i></i></div>

<section class="abs card welcome">
  <h2>Welcome</h2>
  <p>QUILLBROOK &amp; ASSOCIATES, P.C. handles only labor, employment and benefits matters. This includes representing employers in state and federal court before administrative and quasi-judicial agencies and in negotiations..<br>Our attorneys provide a diverse range of counseling and training in areas of the law such as discrimination, sexual harassment, wage and hour issues, Family and Medical Leave Act, HIPPA and reductions-in-force.</p>
  <div class="photo" role="img" aria-label="Scales of justice and a gavel on a flag"></div>
  <span class="btn">Read More</span>
</section>

<section class="abs card news">
  <h2>Latest News</h2>
  <div class="news-item i1"><div class="date">07 April 2015</div><p>Vestibulum ante ipsum primis in faucibus orci luctuset ultrices posuere cubilia ...</p><div class="more">Read More</div></div>
  <div class="news-item i2"><div class="date">07 April 2015</div><p>Vestibulum ante ipsum primis in faucibus orci luctu-set ultrices posuere cubilia ...</p><div class="more">Read More</div></div>
  <span class="btn">Read More</span>
</section>

<div class="abs section"></div>
<section class="abs practice">
  <h2>Area of Practice</h2>
  <p class="lead">Our attorneys provide a diverse range of counseling and training in areas of the law such as discrimination, sexual harassment, wage and hour issues, Family and Medical Leave Act, HIPPA and reductions-in-force.</p>
  <ul class="plist pl1"><li>Employment Law</li><li>Benefits/ERISA Law</li><li>Civil Litigation</li><li>Railway Labor Act</li><li>Hotel Law</li><li>Non-Profit Law</li><li>Federal False Claims Act (Qui Tam)</li></ul>
  <ul class="plist pl2"><li>Construction</li><li>Manufacturing</li><li>Automotive</li><li>Retail</li><li>Non Profits and Religious Organizations</li><li>Financial and Banking Services</li><li>Computer Software Services</li></ul>
  <span class="btn">Read More</span>
</section>
<div class="abs divider"></div>
<section class="abs attorneys">
  <h2>Attorneys</h2>
  <p class="lead">A small team of specialised advocates is focused in selected areas of practice.</p>
  <div class="acard" style="left:0;top:60px"><div class="pic" role="img" aria-label="Attorney portrait"></div><div class="name">Marcus Hale</div><div class="role">Director</div><div class="deg">LL.B., MSc, TEP</div></div>
  <div class="acard" style="left:191px;top:60px"><div class="pic" role="img" aria-label="Attorney portrait"></div><div class="name">Marcus Hale</div><div class="role">Director</div><div class="deg">LL.B., MSc, TEP</div></div>
  <div class="acard" style="left:0;top:136px"><div class="pic" role="img" aria-label="Attorney portrait"></div><div class="name">Marcus Hale</div><div class="role">Director</div><div class="deg">LL.B., MSc, TEP</div></div>
  <div class="acard" style="left:191px;top:136px"><div class="pic" role="img" aria-label="Attorney portrait"></div><div class="name">Marcus Hale</div><div class="role">Director</div><div class="deg">LL.B., MSc, TEP</div></div>
  <span class="btn">View All</span>
</section>

<footer class="abs footer">
  <div class="fcol" style="left:57px"><h3>Quick Links</h3><div>Home<br>Attorneys<br>Areas of Practice »<br>In The News<br>FAQ<br>For Employers<br>Contact Us</div></div>
  <div class="fcol" style="left:182px"><h3>Admissions</h3><div>New York State<br>Eastern District of New York<br>Southern District of New York<br>United States Court of Appeals for the Second Circuit<br>United States Court of Federal Claims<br>United States Supreme Court</div></div>
  <div class="fcol" style="left:434px"><h3>Associations</h3><div>Empire Valley Bar Society<br>Harborline County Bar Society<br>Eastshore County Bar Society<br>Continental Trial Counsel Guild<br>National Workplace Counsel Forum</div></div>
  <div class="fcol" style="left:683px"><h3>Connect us</h3><div class="social"><i></i><i></i><i></i><i></i></div></div>
</footer>
<div class="abs bottom"><span class="copy">Copyright © 2015. All Rights Reserved. Quillbrook &amp; Associates, P.C.</span><span class="legal">Privacy Policy | Disclaimer</span></div>

</body>
</html>
```